I am seeking a book cover design for a new book series. The book deals with life and the principles and essentials that we must have in our lives in order to be happy and have a successful life. Some of the tenets will include 'Spirit' Believe' 'Trust' 'Harmony' 'Family' etc...

I would like to have some natural scene in the background (i.e. water, moutains, forest...that is a ZEN or purity feel)

The '24' should be pronounced in the title in within the foreground of the book cover.

I am open to colors but would like the coloring to emphasize attention. Colors such as forest greens, peaches, pomegranites, are ones that come to mind but i am completely open since it must fit the design.

I will also be looking to do a web design and other additional logos/designs in the coming months so this is a long term opportunity with the right design and communication. I look forward to working with a great partner on this project.

Reason: I am extending the deadline to allow designers who inquired to get their designs submitted. Also to allow several designers to submit changes to their design.

Target Market(s)

Spiritual - Age range 18-80 - Forward Thinkers - Degreed - All cultures and religions

Industry/Entity Type

Communication

Requirements
Must have
• The title 'The Amber Lantern Road'

My Name as the Author: Dovan Pruett

the thoughts should also include a backcover copy consistent with the front and a theme design for the Series.
The book is expected to be 5 1/2 x 8 1/2"
Nice to have
• The book will be released in a series format as well as the entire Amber Lantern. As a suggestion, the books released as part of an individual essential would have the name of that essential referenced on the book. Example (BELEIVE). You may take that into consideration when designing for he cover. Thank you.

```html
<!DOCTYPE html>
<html lang="en">
<head>
<meta charset="utf-8">
<title>The Amber Lantern Road — Believe</title>
<link rel="stylesheet" href="https://fonts.googleapis.com/css2?family=EB+Garamond:wght@400;500&family=Arimo:wght@400&display=swap">
<style>
  :root {
    --lime: #e4fc00;
    --blush: #f9e9f9;
    --paper: #ffffff;
    --maroon: #5b0a0e;
    --numeral: #ededed;
    --mint: #5de9b0;
    --violet: #a95ad0;
    --violet-deep: #5a2a6e;
    --olive: #86aa1c;
    --olive-deep: #3e4a10;
    --sky: #2f8fd8;
    --sky-deep: #1f6fb6;
  }
  * { margin: 0; padding: 0; box-sizing: border-box; }
  html, body { width: 886px; height: 1200px; overflow: hidden; background: var(--paper); }
  .cover { position: relative; width: 886px; height: 1200px; background: var(--paper); overflow: hidden; }

  .accent-bar { position: absolute; left: 0; top: 0; width: 94px; height: 517px; background: var(--lime); }
  .title-panel { position: absolute; left: 115px; top: 0; width: 507px; height: 517px; background: var(--blush); }

  .volume-numeral {
    position: absolute; right: 28px; top: -40px;
    font-family: "EB Garamond", Georgia, serif; font-size: 560px; line-height: 1;
    color: var(--numeral);
  }

  .title { position: absolute; left: 149px; top: 108px; color: var(--maroon);
    font-family: "EB Garamond", Georgia, serif; font-weight: 500; line-height: 1; }
  .title-line { display: block; font-size: 58px; letter-spacing: -0.5px; }
  .title-line + .title-line { margin-top: 8px; }
  .title-emphasis { font-size: 84px; letter-spacing: -1px; }

  .essential {
    position: absolute; left: 146px; top: 348px;
    font-family: "Arimo", Arial, sans-serif; font-size: 104px; line-height: 1;
    color: var(--maroon); letter-spacing: 1px;
  }

  .author-box { position: absolute; left: 622px; top: 458px; width: 264px; height: 59px;
    background: var(--lime); display: flex; align-items: center; justify-content: center; }
  .author { font-family: "EB Garamond", Georgia, serif; font-size: 31px; color: var(--maroon); }

  .scene {
    position: absolute; left: 0; top: 517px; width: 886px; height: 683px;
    background: linear-gradient(to bottom,
      #a8f5d8 0px, var(--mint) 112px,
      var(--paper) 112px, var(--paper) 117px,
      #c98be6 117px, var(--violet) 200px, var(--violet-deep) 342px,
      var(--olive) 342px, var(--olive-deep) 528px,
      var(--sky) 528px, var(--sky-deep) 683px);
  }
</style>
</head>
<body>
  <main class="cover">
    <div class="accent-bar"></div>
    <div class="title-panel"></div>
    <div class="volume-numeral" aria-hidden="true">1</div>

    <h1 class="title">
      <span class="title-line">The <span class="title-emphasis">Amber</span></span>
      <span class="title-line">Lantern</span>
      <span class="title-line">Road</span>
    </h1>
    <h2 class="essential">BELIEVE</h2>

    <div class="author-box"><p class="author">Dovan Pruett</p></div>

    <div class="scene" role="img" aria-label="Calm lake at dusk with hills, silhouetted trees and reeds, tinted in bands of mint, violet, green and blue"></div>
  </main>
</body>
</html>
```